Sales and Lettings Boards

Hello, please see attached our sales and lettings boards for our estate agency. These were "designed" by the sign writers. As you can see they are pretty flat and boring - could you work your magic and make them stand out please? I've also attached the logo files. Many thanks, Dean

Target Market(s)

Consumers - residential sale property sales and lettings

Industry/Entity Type

Real Estate Agent

```html
<!DOCTYPE html>
<html lang="en">
<head>
<meta charset="utf-8">
<title>Verano Sales &amp; Lettings Boards</title>
<link rel="stylesheet" href="https://fonts.googleapis.com/css2?family=Exo+2:wght@300;400;600&family=Russo+One&display=swap">
<style>
  :root {
    --page-bg: #ffffff;
    --board-top: #4d4d4d;
    --board-bottom: #000000;
    --panel-white: #ffffff;
    --brand-grey: #444444;
    --brand-green: #5fad2f;
    --edge: #9a9a9a;
  }
  * { margin: 0; padding: 0; box-sizing: border-box; }
  html, body {
    width: 1200px; height: 1000px; overflow: hidden;
    background: var(--page-bg);
    font-family: "Exo 2", sans-serif;
  }
  .canvas { position: relative; width: 1200px; height: 1000px; }

  .board {
    position: absolute;
    width: 452px; height: 361px;
    background: linear-gradient(180deg, var(--board-top) 0%, #2a2a2a 55%, var(--board-bottom) 100%);
    outline: 1px solid var(--edge);
    overflow: hidden;
  }
  .board--sale  { left: 105px; top: 120px; }
  .board--rooms { left: 643px; top: 120px; }
  .board--let   { left: 374px; top: 537px; }

  .board__shapes { position: absolute; inset: 0; width: 100%; height: 100%; }

  .brand {
    position: absolute; right: 22px; top: 6px;
    display: flex; align-items: center; gap: 10px;
  }
  .brand__dot { width: 20px; height: 20px; border-radius: 50%; background: var(--brand-green); }
  .brand__name {
    font-family: "Exo 2", sans-serif; font-weight: 600;
    font-size: 74px; line-height: 1; letter-spacing: 1px;
    color: var(--brand-grey);
  }
  .brand__tagline {
    position: absolute; right: 84px; top: 86px;
    font-weight: 300; font-size: 22px; letter-spacing: 0.5px;
    color: var(--brand-grey);
  }

  .status {
    position: absolute; left: 18px; top: 158px;
    color: var(--panel-white);
  }
  .status--bold {
    font-family: "Russo One", sans-serif;
    font-size: 70px; line-height: 62px; letter-spacing: 2px;
  }
  .status--light {
    left: 16px; top: 190px;
    font-weight: 300; font-size: 52px; line-height: 46px; letter-spacing: 1px;
  }
  .status--light .status__indent { padding-left: 20px; }
  .status__line { display: block; }

  .contact { position: absolute; right: 18px; top: 285px; text-align: right; }
  .contact__phone {
    display: block; font-weight: 400; font-size: 35px; line-height: 40px;
    letter-spacing: 1px; color: var(--brand-green);
  }
  .contact__web {
    display: block; font-weight: 400; font-size: 22px; line-height: 28px;
    color: var(--panel-white);
  }
</style>
</head>
<body>
<main class="canvas">

  <section class="board board--sale">
    <svg class="board__shapes" viewBox="0 0 452 361" aria-hidden="true">
      <line x1="4" y1="0" x2="286" y2="234" stroke="#ffffff" stroke-width="7"/>
      <polygon points="22,0 452,0 452,108 296,252 14,4" fill="#ffffff"/>
      <line x1="14" y1="2" x2="296" y2="236" stroke="#444444" stroke-width="7"/>
      <line x1="314" y1="256" x2="452" y2="122" stroke="#5fad2f" stroke-width="5"/>
    </svg>
    <div class="brand"><span class="brand__name">VERANO</span></div>
    <p class="brand__tagline">sales &amp; lettings</p>
    <h2 class="status status--bold"><span class="status__line">FOR</span><span class="status__line">SALE</span></h2>
    <p class="contact"><span class="contact__phone">01632 960418</span><span class="contact__web">www.verano-estates.co.uk</span></p>
  </section>

  <section class="board board--rooms">
    <svg class="board__shapes" viewBox="0 0 452 361" aria-hidden="true">
      <line x1="4" y1="0" x2="286" y2="234" stroke="#ffffff" stroke-width="7"/>
      <polygon points="22,0 452,0 452,108 296,252 14,4" fill="#ffffff"/>
      <line x1="14" y1="2" x2="296" y2="236" stroke="#444444" stroke-width="7"/>
      <line x1="314" y1="256" x2="452" y2="122" stroke="#5fad2f" stroke-width="5"/>
    </svg>
    <div class="brand"><span class="brand__name">VERANO</span></div>
    <p class="brand__tagline">sales &amp; lettings</p>
    <h2 class="status status--light"><span class="status__line">ROOMS</span><span class="status__line status__indent">TO LET</span></h2>
    <p class="contact"><span class="contact__phone">01632 960418</span><span class="contact__web">www.verano-estates.co.uk</span></p>
  </section>

  <section class="board board--let">
    <svg class="board__shapes" viewBox="0 0 452 361" aria-hidden="true">
      <line x1="4" y1="0" x2="286" y2="234" stroke="#ffffff" stroke-width="7"/>
      <polygon points="22,0 452,0 452,108 296,252 14,4" fill="#ffffff"/>
      <line x1="14" y1="2" x2="296" y2="236" stroke="#444444" stroke-width="7"/>
      <line x1="314" y1="256" x2="452" y2="122" stroke="#5fad2f" stroke-width="5"/>
    </svg>
    <div class="brand"><span class="brand__name">VERANO</span></div>
    <p class="brand__tagline">sales &amp; lettings</p>
    <h2 class="status status--bold"><span class="status__line">TO</span><span class="status__line">LET</span></h2>
    <p class="contact"><span class="contact__phone">01632 960418</span><span class="contact__web">www.verano-estates.co.uk</span></p>
  </section>

</main>
</body>
</html>
```